Pagina Lartécnica

The Lartécnica is a company dealing with leasing and selling real estate. The current site can be accessed at www.lartecnica-exemplo.com.br. We intend to redesign the look of the site and for that we would like to redesign the home page and the page with information and pictures of the property. The homepage should maintain the characteristics of the current common design simple, short and straightforward. The page with the data of the properties should be accessed with two changes page as it is currently running. The search from the map by region and should be maintained.
The page containing the information of the property will provide a total of 15 small pictures that when clicked will appear in larger size. The colors to be used should be orange, blue, black and white. The map can be maintained in the current colors.
Updates

Project Deadline Extended
Reason: Payment guarante!!

Payment guaranteed. Deadline for submission of designs April 27.

Industry/Entity Type

Real Estate

Requirements
Must have
• Search by map regions and search box
address
keep colors from the current page
phones
clean look
Nice to have
• clean look
Should not have
• We like the current page. We just want to make it compatible with modern and new design trends and monitors.

```html
<!DOCTYPE html>
<html lang="pt">
<head>
<meta charset="utf-8">
<title>Lartécnica – Imóveis</title>
<link href="https://fonts.googleapis.com/css2?family=Source+Sans+3:wght@400;600;700&family=Roboto+Condensed:wght@700&display=swap" rel="stylesheet">
<style>
:root{
  --orange:#f5871f;
  --orange-dark:#e06f0c;
  --navy:#3e3c5e;
  --navy-dark:#2f2d4a;
  --ink:#2b2b33;
  --text:#555;
  --muted:#777;
  --line:#e3e3e6;
  --band:#eeeef1;
  --footer:#3a3a3c;
}
*{box-sizing:border-box;margin:0;padding:0}
html,body{width:797px;height:1200px;overflow:hidden}
body{position:relative;background:#fff;font-family:"Source Sans 3",sans-serif;color:var(--text)}
.abs{position:absolute}
.top-bar{left:0;top:0;width:797px;height:4px;background:var(--orange)}
.band{left:0;top:4px;width:797px;height:313px;background:linear-gradient(#fff,var(--band))}
.logo{left:44px;top:38px;display:flex;align-items:center;gap:8px;font-size:28px;font-weight:700;color:var(--navy);letter-spacing:-.5px}
.logo .mark{width:18px;height:18px;background:var(--orange)}
.phones{right:54px;top:46px;text-align:right;font-size:14.5px;line-height:19px;color:var(--ink)}
.phones span{color:var(--orange);font-size:11.5px}
.nav{left:44px;top:95px;width:709px;height:39px;background:linear-gradient(var(--navy),var(--navy-dark));display:flex;border-radius:2px}
.nav a{color:#fff;text-decoration:none;font-size:12px;white-space:nowrap;display:flex;align-items:center;justify-content:center;border-right:1px solid #55537a}
.nav a:last-child{border:none}
.hero{left:43px;top:134px;width:710px;height:275px;background:#fff;box-shadow:0 1px 3px rgba(0,0,0,.12)}
.hero-photo{left:50px;top:140px;width:695px;height:261px;background:linear-gradient(#bcd8ef 0%,#e9ecea 35%,#d9c8a8 60%,#7b8f54 85%,#9c3a40 100%)}
.dots{left:372px;top:387px;display:flex;gap:4px}
.dots i{width:10px;height:10px;border-radius:50%;background:#fff;display:block}
.dots i:first-child{background:var(--navy)}
.search{left:531px;top:284px;width:214px;height:117px;background:rgba(255,255,255,.94);padding:16px 20px}
.search h3{font-family:"Roboto Condensed",sans-serif;font-size:14px;color:var(--ink);text-transform:uppercase}
.radios{display:flex;gap:14px;font-size:8.5px;margin-top:5px;color:var(--ink)}
.radios b{display:inline-block;width:8px;height:8px;border:1px solid #999;border-radius:50%;margin-right:2px;vertical-align:-1px;font-weight:400}
.field{margin-top:8px;height:20px;background:var(--navy);color:#fff;font-size:7.5px;padding:6px 9px}
.btn{background:var(--orange);color:#fff;font-size:9.5px;display:inline-flex;align-items:center;justify-content:center;border-radius:2px}
.search .btn{position:absolute;right:28px;top:84px;width:68px;height:19px}
h2.caps{font-family:"Roboto Condensed",sans-serif;font-size:16px;color:var(--navy);text-transform:uppercase}
.latest{left:45px;top:432px}
.props{left:44px;top:458px;display:flex;gap:8.5px}
.prop{width:116px}
.thumb{height:92px;background:linear-gradient(#a7c8e8,#d8d4c8 55%,#5d8a3a)}
.prop h4{font-weight:400;font-size:10.5px;color:var(--ink);margin-top:7px}
.prop p{font-size:9px;margin-top:3px}
.prop .btn{width:60px;height:20px;margin-top:6px;font-size:8.5px}
.welcome{left:45px;top:642px;width:485px}
.welcome h1{font-weight:400;font-size:17.5px;color:var(--ink)}
.welcome h5{font-weight:400;font-size:11px;color:var(--ink);margin-top:10px}
.welcome p{font-size:9.2px;line-height:16.5px;margin-top:7px}
.best-title{left:46px;top:771px;font-weight:400;font-size:17px;color:var(--ink)}
.item{left:46px;width:480px;height:86px;display:flex;gap:11px;border-bottom:1px dashed #c9c9c9}
.item.last{border:none}
.item .pic{width:111px;height:68px;flex:none;background:linear-gradient(#b6cfe6,#c9c7c0 50%,#6f7e5a)}
.item h4{font-weight:400;font-size:11px;color:var(--ink);margin-top:1px}
.item p{font-size:9.2px;line-height:17px;margin-top:3px}
.item a{color:var(--orange-dark);font-size:9.2px;text-decoration:none;display:block;margin-top:3px}
.region{left:551px;top:422px;width:199px;height:263px;border:1px solid var(--line)}
.box-head{height:34px;background:linear-gradient(#f9962f,var(--orange));color:#fff;font-size:13.5px;padding:9px 17px}
.map{position:absolute;left:17px;top:45px;width:164px;height:177px;border:3px solid #fff;box-shadow:0 0 0 1px #ddd;background:linear-gradient(120deg,#5a9bd8 0%,#9ccbe8 30%,#efe6c8 48%,#b5d7a4 60%,#6aa8de 80%)}
.region .cta{position:absolute;left:17px;top:230px;width:164px;display:flex;justify-content:space-between;align-items:center;font-size:9.5px}
.region .cta .btn{background:var(--navy);width:58px;height:20px;font-size:9px}
.news{left:551px;top:700px;width:200px;height:248px;border:1px solid var(--line)}
.news .head{height:33px;background:linear-gradient(#fff,#f0f0f2);color:var(--orange-dark);font-size:14.5px;padding:9px 14px}
.news ul{list-style:none;padding:12px 14px 0 14px}
.news li{margin-bottom:15px}
.news li h6{font-weight:400;font-size:9.5px;color:var(--ink)}
.news li p{font-size:8.2px;line-height:15px;margin-top:2px;color:var(--muted)}
.contact{left:562px;top:964px;width:200px;font-size:9.5px;line-height:16px;color:var(--ink);font-style:normal}
.contact h3{font-weight:400;font-size:14.5px;color:var(--orange-dark);margin-bottom:6px}
.contact b{display:block;font-weight:600;font-size:10.5px;margin-bottom:5px}
.footer{left:0;top:1110px;width:797px;height:90px;background:var(--footer)}
.foot-links{left:43px;top:1137px;font-size:10.5px;color:#fff}
.foot-links span{color:#aaa;margin:0 5px}
.copy{left:43px;top:1160px;font-size:7.5px;color:#ccc}
.social{left:692px;top:1142px;display:flex;gap:4px}
.social i{width:18px;height:17px;border-radius:3px;background:#3e8fd6;display:block}
.social i:last-child{background:#3b5b9c}
</style>
</head>
<body>
<div class="abs top-bar"></div>
<div class="abs band"></div>

<div class="abs logo"><span class="mark"></span>Lartécnica</div>
<div class="abs phones"><span>Lease:</span> (48) 3000-0142<br><span>Sales:</span> (48) 9000-0175</div>

<nav class="abs nav">
  <a style="width:66px">HOME</a><a style="width:77px">ABOUT US</a><a style="width:105px">PROPERTY LIST</a><a style="width:79px">LOCATION</a><a style="width:118px">RESTRICTED AREA</a><a style="width:160px">REQUEST YOUR PROPERTY</a><a style="width:104px">CONTACT US</a>
</nav>

<div class="abs hero"></div>
<div class="abs hero-photo" role="img" aria-label="Two-storey cream house with tiled roof, blue garage doors and flowering garden"></div>
<div class="abs dots"><i></i><i></i><i></i><i></i></div>
<div class="abs search">
  <h3>Search for Properties</h3>
  <div class="radios"><span><b></b>to buy</span><span><b></b>Rent</span></div>
  <div class="field">type text here..</div>
  <span class="btn">Search Now</span>
</div>

<h2 class="abs caps latest">Latest Properties</h2>
<div class="abs props">
  <div class="prop"><div class="thumb" role="img" aria-label="Suburban house with lawn"></div><h4>Property Name</h4><p>Location &amp; Area</p><span class="btn">Book Now</span></div>
  <div class="prop"><div class="thumb" role="img" aria-label="Modern house with garage"></div><h4>Property Name</h4><p>Location &amp; Area</p><span class="btn">Book Now</span></div>
  <div class="prop"><div class="thumb" role="img" aria-label="House with front porch"></div><h4>Property Name</h4><p>Location &amp; Area</p><span class="btn">Book Now</span></div>
  <div class="prop"><div class="thumb" role="img" aria-label="House with red roof among trees"></div><h4>Property Name</h4><p>Location &amp; Area</p><span class="btn">Book Now</span></div>
</div>

<section class="abs welcome">
  <h1>Welcome to Our Website Mainpage..</h1>
  <h5>Etiam est nunc, venenatis in, tristique eu, imperdiet ac, nisl.</h5>
  <p>Nulla elementum dui ut augue. Aliquam vehicula mi at mauris. Maecenas placerat, nisl at consequat rhoncus, sem nunc gravida justo, quis eleifend arcu velit quis lacus. Morbi magna magna, tincidunt a, mattis non, imperdiet vitae, tellus. Sed odio est, auctor ac, sollicitudin in, consequat vitae, orci. Fusce id felis. Vivamus sollicitudin metus eget eros.</p>
</section>

<h2 class="abs best-title">Best Property</h2>
<div class="abs item" style="top:801px"><div class="pic" role="img" aria-label="Grey two-storey family house"></div><div><h4>Property Tittle here</h4><p>Nulla elementum dui ut augue. Aliquam vehicula mi at mauris. Maecenas placerat, nisl at consequat rhoncus, sem nunc gravida justo, quis eleifend arcu velit quis lacus.</p><a>Learn More</a></div></div>
<div class="abs item" style="top:900px"><div class="pic" role="img" aria-label="Craftsman style house with garden"></div><div><h4>Property Tittle here</h4><p>Nulla elementum dui ut augue. Aliquam vehicula mi at mauris. Maecenas placerat, nisl at consequat rhoncus, sem nunc gravida justo, quis eleifend arcu velit quis lacus.</p><a>Learn More</a></div></div>
<div class="abs item last" style="top:1002px"><div class="pic" role="img" aria-label="White modern house with balconies"></div><div><h4>Property Tittle here</h4><p>Nulla elementum dui ut augue. Aliquam vehicula mi at mauris. Maecenas placerat, nisl at consequat rhoncus, sem nunc gravida justo, quis eleifend arcu velit quis lacus.</p><a>Learn More</a></div></div>

<aside class="abs region">
  <div class="box-head">Search Property by Region</div>
  <div class="map" role="img" aria-label="Regional map of the island and coast"></div>
  <div class="cta"><span>Click here to Search now</span><span class="btn">Click here</span></div>
</aside>

<aside class="abs news">
  <div class="head">Recent Project News</div>
  <ul>
    <li><h6>Are You Ready for Your Server to Fail?</h6><p>Nunc tempus felis vitae urna. Vivamus porttitor, g, purus nisi eleifend libero,</p></li>
    <li><h6>Etiam est nunc venenatis</h6><p>Vivamus porttitor, g, purus nisi eleifend libero, a tempus libero lectus feugiat felis.</p></li>
    <li><h6>Mauris vel lacus vitae</h6><p>Nunc tempus felis vitae urna. Vivamus porttitor, g, purus nisi eleifend libero, a tempus libero lectus feugiat felis.</p></li>
  </ul>
</aside>

<address class="abs contact">
  <h3>Contact Information</h3>
  <b>Lartécnica</b>
  Rua das Acácias, 140 - Esquina com a Rua do Porto - Centro - Florianópolis<br>
  Phone no. &nbsp;(48) 3000-0142<br>
  Sales no. &nbsp;(48) 9000-0175
</address>

<footer class="abs footer"></footer>
<div class="abs foot-links">Home<span>|</span>About Us<span>|</span>Services<span>|</span>Blog<span>|</span>Testimonials<span>|</span>News<span>|</span>Projects<span>|</span>Support<span>|</span>Contact</div>
<div class="abs copy">Copyright © 2013 Company Name. &nbsp;All right reserved. &nbsp;Term of Use</div>
<div class="abs social"><i></i><i></i><i></i></div>
</body>
</html>
```